Online Rug Store needs Clearance Banner

Website is: Marvelous Mats and Interiors
You can access it at: www.marvelousmatsandinteriors-example.com and login (top right) with password: plorvat

*** update: When creating banners for my site, you have permission to use images from www.kelvora-example.com, but ONLY for this project. The images/artwork are copyright allowable for use on www.marvelousmatsandinteriors-example.com projects.***

We need a home page banner sized 1000 wide x 500 tall pixels to promote a "Clearance Sale" on rugs. The banner can state:

1. Clearance Sale
2. Now in progress
3. Save an extra 20% with coupon code 'Take20'
4. Ends March 31st
5. Plus Free Shipping and 30 day returns.

We prefer a banner that appears hand-drawn and artistic, not commercially produced. It is OK to use a room scene image, rug images, or just a colored/textured background with text and no images. Your choice.

Flat graphics with no shadows and 3-D effect preferred.
Attached is are 3 logo options, as well as an example banner with handcrafted, artistic styling that we prefer.

Target Market(s)

This should be an eye-catching banner to showcase a very urgent promotion. Consider using colors of red, white, gold, and black to make a strong statement on the home page.

Industry/Entity Type

Home And Garden

Requirements
Must have
• Winner must provide Photoshop editable file format (.psd format) including layers that can be edited.
Nice to have
• Hand-drawn, stenciled, scribbled, artistic graphics and fonts is nice because we sell rugs that are made by hand.
Should not have
• little to no shadowing. Avoid computerized graphics.

```html
<!DOCTYPE html>
<html lang="en">
<head>
<meta charset="utf-8">
<title>Clearance Sale Banner</title>
<link href="https://fonts.googleapis.com/css2?family=Antonio:wght@400;500&display=swap" rel="stylesheet">
<style>
  :root {
    --page-bg: #b8888b;
    --frame: #fbf5df;
    --rug-light: #b2513a;
    --rug-mid: #8e3328;
    --rug-deep: #5e2322;
    --rug-dark: #3e1a1f;
    --type: #fbf6e2;
    --type-shadow: #3a1410;
  }
  html, body {
    margin: 0;
    padding: 0;
    width: 1200px;
    height: 1200px;
    overflow: hidden;
    background: var(--page-bg);
  }
  .canvas {
    display: block;
    width: 1200px;
    height: 1200px;
  }
  .banner-frame { fill: var(--frame); }
  .sale-type {
    font-family: "Antonio", "Arial Narrow", sans-serif;
    font-weight: 500;
    fill: var(--type);
    filter: drop-shadow(3px 3px 0 var(--type-shadow));
  }
</style>
</head>
<body>
<svg class="canvas" viewBox="0 0 1200 1200" xmlns="http://www.w3.org/2000/svg">
  <defs>
    <linearGradient id="rugTones" x1="0" y1="0" x2="1" y2="0.3">
      <stop offset="0" stop-color="var(--rug-light)"/>
      <stop offset="0.4" stop-color="var(--rug-mid)"/>
      <stop offset="0.75" stop-color="var(--rug-deep)"/>
      <stop offset="1" stop-color="var(--rug-dark)"/>
    </linearGradient>
  </defs>

  <g class="banner" transform="translate(40 321)">
    <rect class="banner-frame" x="0" y="0" width="1120" height="558"/>
    <rect class="banner-rug" x="6" y="6" width="1108" height="546" fill="url(#rugTones)"
          role="img" aria-label="Close-up photo of a patchwork rug in faded red, rust and dark plum panels"/>

    <g class="headline">
      <text class="sale-type" x="118" y="188" font-size="150" textLength="360" lengthAdjust="spacingAndGlyphs">CLEARANCE</text>
      <text class="sale-type" x="118" y="383" font-size="232" textLength="360" lengthAdjust="spacing">SALE</text>
      <text class="sale-type" x="118" y="478" font-size="100" textLength="360" lengthAdjust="spacingAndGlyphs">END MARCH 31ST</text>
    </g>

    <g class="offer">
      <text class="sale-type" x="610" y="122" font-size="58" textLength="389" lengthAdjust="spacingAndGlyphs">SAVE AN EXTRA 20%</text>
      <text class="sale-type" x="610" y="190" font-size="64" textLength="389" lengthAdjust="spacingAndGlyphs">WITH COUPON CODE</text>
      <text class="sale-type" x="610" y="346" font-size="168" textLength="389" lengthAdjust="spacingAndGlyphs">'TAKE20'</text>
      <text class="sale-type" x="610" y="413" font-size="62" textLength="389" lengthAdjust="spacingAndGlyphs">PLUS FREE SHIPPING</text>
      <text class="sale-type" x="610" y="478" font-size="62" textLength="389" lengthAdjust="spacingAndGlyphs">AND 30 DAY RETURNS</text>
    </g>
  </g>
</svg>
</body>
</html>
```